Northgate Hoopers Needs Post Card Announcing Basketball Try Outs

TEXT
NORTHGATE HOOPERS
...a Riverbend Outreach Alliance Inc. program
(approved IRS 501C3)

BRAND NEW YCL Member Organization
Invites All Ballers / Boys and Girls / 2nd - 11th Grades

Open Gym Tryouts Start June 2014

Register for tryouts and join our emailing list by contacting us at....northgatehoopers@mailbrook.net

Phone Contact Marcus Delaney.(555) 482-3907
or visit us at www.northgatehoopers.net

```html
<!DOCTYPE html>
<html lang="en">
<head>
<meta charset="utf-8">
<title>Northgate Hoopers – Post Card</title>
<link rel="stylesheet" href="https://fonts.googleapis.com/css2?family=Oswald:wght@700&family=Open+Sans:wght@400;700&family=Cabin:wght@500&display=swap">
<style>
  :root {
    --paper: #ffffff;
    --ink: #111111;
    --brand-blue: #1f3f9a;
    --deep-blue: #26307a;
    --card-blue: #3c3f94;
    --stamp-blue: #3a45a0;
    --accent-red: #d3212b;
  }
  * { margin: 0; padding: 0; box-sizing: border-box; }
  html, body { width: 1200px; height: 931px; overflow: hidden; background: var(--paper); }
  .postcard { position: relative; width: 1200px; height: 931px; background: var(--paper); }

  .league-mark {
    position: absolute; left: 26px; top: 104px;
    display: flex; align-items: center; gap: 10px;
  }
  .league-mark__square { width: 22px; height: 22px; background: var(--accent-red); }
  .league-mark__name {
    font-family: "Open Sans", sans-serif; font-weight: 700;
    font-size: 34px; color: var(--brand-blue); line-height: 1;
  }

  .sender { position: absolute; left: 171px; top: 64px; }
  .sender__team {
    font-family: "Oswald", sans-serif; font-weight: 700;
    font-size: 27px; letter-spacing: 2px; color: var(--brand-blue);
    line-height: 1;
  }
  .sender__contact {
    margin-top: 19px;
    font-family: "Open Sans", sans-serif; font-size: 23px;
    color: var(--deep-blue); line-height: 1;
  }
  .sender__details {
    margin-top: 12px;
    font-family: "Open Sans", sans-serif; font-size: 19.5px;
    color: var(--ink); line-height: 32px;
  }

  .divider-text {
    position: absolute; left: 598px; top: 450px;
    transform: translate(-50%, -50%) rotate(-90deg);
    white-space: nowrap;
    font-family: "Open Sans", sans-serif; font-weight: 700;
    font-size: 11.5px; letter-spacing: 2.3px; color: var(--ink);
  }

  .postcard__label {
    position: absolute; left: 628px; top: 240px;
    font-family: "Cabin", sans-serif; font-weight: 500;
    font-size: 54px; color: var(--card-blue); line-height: 1;
  }

  .stamp-box {
    position: absolute; left: 1003px; top: 65px;
    width: 163px; height: 183px; background: var(--stamp-blue);
    display: flex; flex-direction: column; align-items: center;
    padding-top: 36px; gap: 19px;
    font-family: "Open Sans", sans-serif; font-size: 20px;
    color: var(--paper); line-height: 1;
  }
</style>
</head>
<body>
  <main class="postcard">
    <div class="league-mark">
      <span class="league-mark__square"></span>
      <span class="league-mark__name">YCL</span>
    </div>

    <section class="sender">
      <h1 class="sender__team">NORTHGATE HOOPERS</h1>
      <p class="sender__contact">Marcus Delaney (555) 482-3907</p>
      <p class="sender__details">
        Register for tryouts and join our emailing<br>
        list &nbsp;by contacting us at:<br>
        email: northgatehoopers@mailbrook.net<br>
        visit us at: www.northgatehoopers.net
      </p>
    </section>

    <p class="divider-text">LOREM © PSUM DOLOR SIT AMET, CONSECTETUR ADIPISICING ELIT, SED DO EIUSMOD TEMPOR</p>

    <h2 class="postcard__label">POST CARD</h2>

    <div class="stamp-box">
      <span>PLACE</span>
      <span>STAMP</span>
      <span>HERE</span>
    </div>
  </main>
</body>
</html>
```